Starter & Alternator business needs a website

update: very good designs submitted so far. also need this to display well on mobile devices. not sure if wordpress or html/css is better for my needs.

Our existing website is vexlandrib.com and is need of total revamp. Need full design of a website for my business.

We sell and rebuild starters and alternators. Customers bring in the units and we rebuild them. Or we sell them brand new or rebuilt units we have in stock. We do not install units into vehicles like a mechanic would. We strictly rebuild starters and alternators in our shop, sell brand new units over the counter, and we do deliver occasionally as well. We do offer a line of Morlin batteries as well but that is only a small feature of the business.

I would like this website designed and coded. I can upload the files to my web host after completion. I can also add in and modify content like our background info, etc.

I have included an illustrator file that shows some of our signage and logo, etc. I have also included a radio commercial sample so you can get a little better feel for the business. A similar ad does run on the radio currently, slightly different and without the added sound effects.

Update: I do like using photos of real items(starters or alternators etc) for an icon, like a real alternator stock image for the alternator section icon, etc. Maybe incorporate our logo in that design as well. That looks nice as well and may aid in navigation.

For any other design elements, do what you think looks good. Our colors are red/white/blue as seen in the illustrator file. our building is painted with talbot greaves colors, emberglow red and deep harbor for blue.

Here are some examples of rebuilders websites in other markets for reference:

https://brommelgarage.com/starter-alternator-rebuilding/

https://www.quintonmotorworks.com/auto-repairs/alternator-starter-rebuilds.aspx

https://www.lorvexcharging.com/

https://www.damblingwx.com/

The website can have areas for: services and products offered, high output alternators, Morlin Batteries, troubleshooting tips, current specials, contact info and directions/map, etc. Whatever else you feel applies.

At some point I do want to be able to sell items directly online or at least have a secure section for customers to submit invoice payments, but that's not necessarily in scope for this project just something to keep in mind.

Target Market(s)

Mechanics and Managers in fleet shops, construction and marine industries, shipping trades. Also automobile owners who work on their own vehicles. We sell and rebuild starters and alternators for automobiles, heavy duty equipment, forklifts, gradalls, man movers, bobcats, loaders, large tractors and trucks, just about any engine, golf carts, generators, etc.

Industry/Entity Type

Automotive Part

Coding

Coded - Design and coding required

Number of Pages Required

5+ page

Font styles to use
Serif
Sans Serif

Colors
0255a3
ec1f27
ffffff

Requirements
Must have
• Should also display nicely on mobile phones. Highlight our specialty, "Starters & Alternators"

```html
<!DOCTYPE html>
<html lang="en">
<head>
<meta charset="utf-8">
<title>Vexlandrib – Starters &amp; Alternators</title>
<link href="https://fonts.googleapis.com/css2?family=Roboto:ital,wght@0,300;0,400;0,500;0,700;1,300;1,400&display=swap" rel="stylesheet">
<style>
:root{
  --blue:#0255a3;
  --navy:#0b3c8f;
  --red:#ec1f27;
  --red-card:#e3050f;
  --white:#ffffff;
  --ink:#1c1c1c;
  --grey-card:#efefef;
  --blog-bg:#eeecef;
}
*{margin:0;padding:0;box-sizing:border-box}
html,body{width:1200px;height:3387px;overflow:hidden}
body{font-family:'Roboto',sans-serif;color:var(--ink);background:var(--white);position:relative}
a{color:inherit;text-decoration:none}
.abs{position:absolute}

/* header */
.site-header{position:absolute;left:0;top:0;width:1200px;height:134px;background:var(--white);z-index:3}
.brand{position:absolute;left:100px;top:40px;display:flex;align-items:center;gap:12px;z-index:4}
.brand-dot{width:36px;height:36px;border-radius:50%;background:var(--red)}
.brand-name{font-weight:700;font-size:28px;color:var(--ink);letter-spacing:.5px}
.call{position:absolute;left:712px;top:20px;display:flex;align-items:center;gap:8px}
.call-icon{width:42px;height:42px;border:2px solid var(--navy);border-radius:50%;display:flex;align-items:center;justify-content:center}
.call small{display:block;font-size:12px;font-weight:700}
.call strong{font-size:19px;font-weight:500}
.cart{position:absolute;left:950px;top:30px;font-size:13px;font-weight:700;display:flex;gap:6px;align-items:center}
.search{position:absolute;left:1030px;top:30px;font-size:15px;color:#333;display:flex;gap:8px;align-items:center}
.main-nav{position:absolute;right:102px;top:95px;display:flex;gap:38px;font-size:16px;font-weight:500;letter-spacing:.3px}

/* hero */
.hero{position:absolute;left:0;top:134px;width:1200px;height:586px;background:linear-gradient(110deg,#8ea4b8 0%,#4f7d96 35%,#3f6c86 55%,#9fb0c2 80%,#d6dce6 100%)}
.hero-cut{position:absolute;left:0;top:134px}
.hero-title{position:absolute;left:100px;top:343px;color:var(--white);font-size:30px;font-weight:500}
.hero-sub{position:absolute;left:99px;top:390px;color:var(--white);font-size:19px;font-style:italic;font-weight:300;line-height:26px}
.btn-start{position:absolute;left:99px;top:463px;width:151px;height:35px;background:var(--navy);color:var(--white);font-size:14px;font-weight:700;display:flex;align-items:center;justify-content:center}
.arrow-l,.arrow-r{position:absolute;top:350px}

/* welcome */
.welcome-title{position:absolute;left:104px;top:798px;font-size:30px;font-weight:500;line-height:36px}
.rule{position:absolute;height:3px;width:64px;background:linear-gradient(90deg,var(--navy) 50%,var(--red) 50%)}
.welcome-text{position:absolute;left:100px;top:924px;width:552px;font-size:15.5px;font-style:italic;font-weight:300;line-height:28.3px;text-align:justify;color:#222}
.read-more{position:absolute;left:100px;top:1166px;font-size:16px;font-weight:700;padding-bottom:3px;border-bottom:3px solid;border-image:linear-gradient(90deg,var(--navy) 60%,var(--red) 60%) 1}
.welcome-photo{position:absolute;left:712px;top:828px;width:392px;height:282px;border-radius:30px;background:linear-gradient(150deg,#2f7a4d 0%,#1f5a3a 40%,#6e8da4 70%,#b9c6d2 100%)}

/* services */
.services{position:absolute;left:0;top:1222px}
.services-title{position:absolute;left:523px;top:1313px;color:var(--white);font-size:30px;font-weight:700}
.svc-card{position:absolute;width:328px;height:165px;background:var(--red-card);color:var(--white);padding:20px 38px 0 45px}
.svc-card h3{font-size:13px;font-weight:700;margin-bottom:9px}
.svc-card p{font-size:12.8px;font-style:italic;font-weight:300;line-height:18px;text-align:justify}
.svc-card a{display:block;margin-top:9px;font-size:11px;font-weight:700}
.svc-icon{position:absolute;width:92px;height:92px;border-radius:50%;background:var(--white);border:4px solid #f2d4d5;display:flex;align-items:center;justify-content:center}

/* pricing */
.section-title{position:absolute;width:1200px;text-align:center;font-size:30px;font-weight:500;letter-spacing:2px}
.price-card{position:absolute;top:2063px;width:309px;height:309px;background:var(--grey-card);padding:50px 0 0 40px}
.price-card.featured{background:var(--navy);color:var(--white);overflow:hidden;box-shadow:0 2px 4px rgba(0,0,0,.3)}
.price{font-size:27px;font-weight:500;text-align:center;width:229px}
.plan{font-size:15px;font-weight:700;letter-spacing:1.2px;margin-top:20px}
.features{list-style:none;margin-top:19px;font-size:15px;line-height:30px;letter-spacing:.4px}
.features li::before{content:"*";color:var(--red);font-size:18px;margin-right:6px}
.features li:first-child{font-size:14px}
.buy{position:absolute;left:97px;top:240px;width:116px;height:28px;background:var(--navy);color:var(--white);font-size:15px;font-weight:700;letter-spacing:1px;display:flex;align-items:center;justify-content:center}
.featured .buy{background:var(--red)}
.ribbon{position:absolute;left:-34px;top:30px;width:150px;height:24px;background:var(--red);transform:rotate(-50deg);color:var(--white);font-size:11px;font-weight:700;display:flex;align-items:center;justify-content:center}

/* blog */
.blog{position:absolute;left:0;top:2477px;width:1200px;height:533px;background:var(--blog-bg)}
.blog-card{position:absolute;top:2608px;width:298px;height:343px;background:var(--white);box-shadow:0 0 3px rgba(0,0,0,.25)}
.blog-photo{height:185px;position:relative}
.blog-photo span{position:absolute;left:12px;bottom:22px;color:var(--white);font-size:10px}
.blog-body{padding:24px 22px 0 23px}
.blog-body h4{font-size:12.5px;font-weight:700;line-height:13px;letter-spacing:.4px}
.blog-body p{font-size:11px;line-height:13px;color:#333;margin-top:10px}
.blog-body a{display:block;margin-top:12px;font-size:13px;font-weight:700;color:var(--navy)}

/* footer */
.footer{position:absolute;left:0;top:3010px}
.f-head{position:absolute;top:3112px;color:var(--white);font-size:17px;font-weight:700;letter-spacing:.5px}
.f-head.big{font-size:21px;top:3108px}
.f-text{position:absolute;color:var(--white);font-style:italic;font-weight:300;font-size:16px;line-height:25.6px}
.f-links{position:absolute;left:413px;top:3150px;list-style:none;color:var(--white);font-style:italic;font-weight:300;font-size:16px;line-height:30px}
.socials{position:absolute;left:616px;top:3269px;display:flex;gap:8px}
.socials span{width:26px;height:26px;border-radius:50%;background:var(--white)}
.pay-name{position:absolute;left:840px;top:3196px;color:var(--white);font-size:30px;font-weight:700}
.pay-cards{position:absolute;left:835px;top:3258px;display:flex;gap:8px}
.pay-cards span{width:60px;height:36px;background:var(--white);border-radius:2px}
.copyright{position:absolute;left:0;top:3345px;width:1200px;height:42px;background:var(--white);text-align:center;font-size:15px;line-height:42px;color:#222}
</style>
</head>
<body>

<header class="site-header">
  <div class="brand"><span class="brand-dot"></span><span class="brand-name">VEXLANDRIB</span></div>
  <div class="call">
    <div class="call-icon">
      <svg width="22" height="22" viewBox="0 0 24 24" fill="none" stroke="#ec1f27" stroke-width="2"><path d="M5 3h4l2 5-3 2a12 12 0 0 0 6 6l2-3 5 2v4a2 2 0 0 1-2 2A17 17 0 0 1 3 5a2 2 0 0 1 2-2z"/></svg>
    </div>
    <div><small>CALL US:</small><strong>(064) 555-0148</strong></div>
  </div>
  <div class="cart">
    <svg width="20" height="18" viewBox="0 0 24 22" fill="none" stroke="#222" stroke-width="2"><path d="M1 2h4l3 12h12l3-9H6"/><circle cx="9" cy="19" r="2"/><circle cx="18" cy="19" r="2"/></svg>(2)
  </div>
  <div class="search">
    <svg width="15" height="15" viewBox="0 0 24 24" fill="none" stroke="#888" stroke-width="2"><circle cx="10" cy="10" r="7"/><path d="M15 15l7 7"/></svg>Search
  </div>
  <nav class="main-nav"><a>HOME</a><a>ABOUT</a><a>SERVICE</a><a>PRODUCT</a><a>SHOP</a><a>CONTACT</a></nav>
</header>

<section>
  <div class="hero" role="img" aria-label="Photo of a cut-away blue electric motor on a workshop bench"></div>
  <svg class="hero-cut" width="1200" height="586"><polygon points="0,586 1200,500 1200,586" fill="#fff"/></svg>
  <svg class="arrow-l" style="left:28px" width="14" height="24"><path d="M12 2 2 12l10 10" fill="none" stroke="#fff" stroke-width="2"/></svg>
  <svg class="arrow-r" style="left:1150px" width="14" height="24"><path d="M2 2l10 10L2 22" fill="none" stroke="#fff" stroke-width="2"/></svg>
  <h1 class="hero-title">STARTERS AND ALTERNATORS</h1>
  <p class="hero-sub">CUSTOMERS BRING IN THE UNITS AND<br>WE REBUILD THEM.</p>
  <a class="btn-start">GET STARTED</a>
</section>

<section>
  <h2 class="welcome-title">WELCOME TO<br>STARTERS AND ALTERNATORS</h2>
  <div class="rule" style="left:106px;top:892px"></div>
  <p class="welcome-text">Lorem Ipsum is simply dummy text of the printing and typesetting industry. Lorem Ipsum has been the industry's standard dummy text ever since the 1500s, when an unknown printer took a galley of type and scrambled it to make a type specimen book. It has survived not only five centuries, but also the leap into electronic typesetting, remaining essentially unchanged. It was popularised in the 1960s with the release of Verrant sheets containing Lorem Ipsum passages, and more recently with desktop publishing software like Holbrin PageSetter including versions of Lorem Ipsum</p>
  <a class="read-more">READ MORE →</a>
  <div class="welcome-photo" role="img" aria-label="Cut-away electric motor showing its green internal windings"></div>
</section>

<section>
  <svg class="services" width="1200" height="640" role="img" aria-label="Dark background photo of stacked alternator rotors">
    <defs><radialGradient id="svcbg" cx="50%" cy="55%" r="70%"><stop offset="0" stop-color="#3a3c42"/><stop offset="1" stop-color="#141519"/></radialGradient></defs>
    <polygon points="0,92 1200,0 1200,640 0,640" fill="url(#svcbg)"/>
  </svg>
  <h2 class="services-title">SERVICES</h2>
  <div class="rule" style="left:560px;top:1365px"></div>

  <div class="svc-card" style="left:187px;top:1446px"><h3>HIGH OUTPUT ALTERNATORS</h3><p>Lorem Ipsum is simply dummy text of the printing and typesetting industry. Lorem Ipsum has been the industry's standard dummy text</p><a>READ MORE »</a></div>
  <div class="svc-card" style="left:733px;top:1446px"><h3>MORLIN BATTERIES</h3><p>Lorem Ipsum is simply dummy text of the printing and typesetting industry. Lorem Ipsum has been the industry's standard dummy text</p><a>READ MORE »</a></div>
  <div class="svc-card" style="left:187px;top:1650px"><h3>CURRENT SPECIALS</h3><p>Lorem Ipsum is simply dummy text of the printing and typesetting industry. Lorem Ipsum has been the industry's standard dummy text</p><a>READ MORE »</a></div>
  <div class="svc-card" style="left:735px;top:1650px"><h3>TROUBLESHOOTING</h3><p>Lorem Ipsum is simply dummy text of the printing and typesetting industry. Lorem Ipsum has been the industry's standard dummy text</p><a>READ MORE »</a></div>

  <div class="svc-icon" style="left:116px;top:1482px"><svg width="50" height="44" viewBox="0 0 50 44" fill="none" stroke="#ec1f27" stroke-width="2.5"><rect x="6" y="10" width="28" height="24" rx="3"/><path d="M34 16h8l5 6-5 6h-8M2 16v12"/></svg></div>
  <div class="svc-icon" style="left:664px;top:1482px"><svg width="48" height="42" viewBox="0 0 48 42" fill="none" stroke="#ec1f27" stroke-width="2.5"><rect x="3" y="10" width="42" height="28" rx="2"/><path d="M10 10V4h8v6M30 10V4h8v6M10 24h10M32 24h8M36 20v8"/></svg></div>
  <div class="svc-icon" style="left:116px;top:1686px"><svg width="50" height="50" viewBox="0 0 50 50" fill="none" stroke="#ec1f27" stroke-width="2.5"><circle cx="25" cy="25" r="21"/><path d="M29 8 16 28h10l-5 14 13-20H24z"/></svg></div>
  <div class="svc-icon" style="left:666px;top:1686px"><svg width="48" height="46" viewBox="0 0 48 46" fill="none" stroke="#ec1f27" stroke-width="2.5"><rect x="3" y="8" width="42" height="34" rx="3"/><path d="M16 8V3h16v5"/><circle cx="24" cy="24" r="7"/><path d="M3 30h14M31 30h14"/></svg></div>
</section>

<section>
  <h2 class="section-title" style="top:1958px;left:0">PRICING</h2>
  <div class="rule" style="left:568px;top:2006px"></div>

  <div class="price-card" style="left:100px">
    <div class="price">$250/-</div><div class="plan">HIGH OUTPUT ALTERNATORS</div>
    <ul class="features"><li>Engine's mechanical energy</li><li>Electrical energy</li><li>Efficient performance.</li></ul>
    <a class="buy">BUY NOW</a>
  </div>
  <div class="price-card featured" style="left:446px">
    <div class="ribbon">SALE 20% OFF</div>
    <div class="price">$250/-</div><div class="plan">MORLIN BATTERIES</div>
    <ul class="features"><li>Engine's mechanical energy</li><li>Electrical energy</li><li>Efficient performance.</li></ul>
    <a class="buy">BUY NOW</a>
  </div>
  <div class="price-card" style="left:790px">
    <div class="price">$250/-</div><div class="plan">TROUBLESHOOTING</div>
    <ul class="features"><li>Engine's mechanical energy</li><li>Electrical energy</li><li>Efficient performance.</li></ul>
    <a class="buy">BUY NOW</a>
  </div>
</section>

<section>
  <div class="blog"></div>
  <h2 class="section-title" style="top:2515px;left:0">LATEST BLOG</h2>
  <div class="rule" style="left:568px;top:2570px"></div>

  <article class="blog-card" style="left:100px">
    <div class="blog-photo" role="img" aria-label="Photo of alternator rotors with copper windings" style="background:linear-gradient(135deg,#3a2a22,#8a5a3c 50%,#2a2a2e)"><span>November 26, 2018</span></div>
    <div class="blog-body"><h4>LOREM IPSUM IS SIMPLY DUMMY TEXT OF THE PRINTING</h4><p>Nunc tempus, auctor mauris montes, attis fringilla dignissim. Vitae habitant estibulum quisque commodo.</p><a>Read More</a></div>
  </article>
  <article class="blog-card" style="left:451px">
    <div class="blog-photo" role="img" aria-label="Photo of starter parts and tools on a workbench" style="background:linear-gradient(135deg,#7a6a5e,#b07a55 50%,#4a4440)"><span>November 26, 2018</span></div>
    <div class="blog-body"><h4>LOREM IPSUM IS SIMPLY DUMMY TEXT OF THE PRINTING</h4><p>Nunc tempus, auctor mauris montes, attis fringilla dignissim. Vitae habitant estibulum quisque commodo.</p><a>Read More</a></div>
  </article>
  <article class="blog-card" style="left:803px">
    <div class="blog-photo" role="img" aria-label="Close-up photo of an armature commutator" style="background:linear-gradient(135deg,#9aa2ae,#6a5a52 50%,#c8ccd4)"><span>November 26, 2018</span></div>
    <div class="blog-body"><h4>LOREM IPSUM IS SIMPLY DUMMY TEXT OF THE PRINTING</h4><p>Nunc tempus, auctor mauris montes, attis fringilla dignissim. Vitae habitant estibulum quisque commodo.</p><a>Read More</a></div>
  </article>
</section>

<footer>
  <svg class="footer" width="1200" height="335"><polygon points="0,55 1200,0 1200,335 0,335" fill="#0b3c8f"/></svg>
  <h3 class="f-head big" style="left:101px">ABOUT</h3>
  <p class="f-text" style="left:101px;top:3150px;width:230px;text-align:justify">Lorem Ipsum is simply dummy text of the printing and typesetting industry. Lorem Ipsum has been the industry's standard dummy text ever since the 1500s</p>
  <h3 class="f-head" style="left:411px">QUICKLINKS</h3>
  <ul class="f-links"><li>Home</li><li>About</li><li>Service</li><li>Product</li><li>Shop</li><li>Contact</li></ul>
  <h3 class="f-head" style="left:591px">CONTACT US</h3>
  <svg class="abs" style="left:593px;top:3155px" width="12" height="16" viewBox="0 0 12 16"><path d="M6 0a6 6 0 0 1 6 6c0 4-6 10-6 10S0 10 0 6a6 6 0 0 1 6-6z" fill="#fff"/><circle cx="6" cy="6" r="2" fill="#0b3c8f"/></svg>
  <p class="f-text" style="left:619px;top:3150px">218 Harlow Lane, USA,<br>New York</p>
  <svg class="abs" style="left:594px;top:3225px" width="16" height="16" viewBox="0 0 24 24" fill="none" stroke="#fff" stroke-width="2"><path d="M5 3h4l2 5-3 2a12 12 0 0 0 6 6l2-3 5 2v4a2 2 0 0 1-2 2A17 17 0 0 1 3 5a2 2 0 0 1 2-2z"/></svg>
  <p class="f-text" style="left:619px;top:3220px">Phone: (064) 555-0148</p>
  <div class="socials"><span></span><span></span><span></span><span></span></div>
  <div class="pay-name">Quorvipay</div>
  <div class="pay-cards"><span></span><span></span><span></span><span></span></div>
  <div class="copyright">Copyrights @ 2019 All Rights Reserved</div>
</footer>

</body>
</html>
```